Branvique needs a business Card Design

We are looking for a business card Design for our new Managed Service Provider Company, Branvique. Branvique encompasses everything IT for the average medium sized business. Our primary services are help desk support, cyber-security (malware and ransomware protection), and Disaster Recovery systems. We would like the design to have a very clean and professional look, with a very minimalist feel.

Target Market(s)

Medium to large sized businesses

Industry/Entity Type

It Service

Contact Information for Business Card

Name GoesHere
name@branvique.com
O: 555-382-6047
C: 555-731-5820

Font styles to use
Other font styles liked:
• Poppins Font Only Please

Colors

Designer to choose only greyscale colors for use in the design.

Requirements
Must have
• Logo included
Nice to have
• Cutting Edge, innovative, minimalistic, elegant

```html
<!DOCTYPE html>
<html lang="en">
<head>
<meta charset="UTF-8">
<title>Branvique Business Card</title>
<link href="https://fonts.googleapis.com/css2?family=Poppins:wght@400;500;600&display=swap" rel="stylesheet">
<style>
  :root {
    --backdrop: #8a8a8a;
    --card-light: #ececec;
    --ink: #1e1e1e;
    --ink-soft: #3a3a3a;
    --card-dark: #232323;
    --paper: #ffffff;
  }
  html, body {
    margin: 0;
    padding: 0;
    width: 1200px;
    height: 1200px;
    overflow: hidden;
    background: var(--backdrop);
    font-family: "Poppins", sans-serif;
  }
  .canvas {
    position: relative;
    width: 1200px;
    height: 1200px;
  }
  .card {
    position: absolute;
    top: 310px;
    width: 364px;
    height: 593px;
    box-shadow: 2px 3px 6px rgba(0, 0, 0, 0.35);
  }
  .card--front {
    left: 234px;
    background: var(--card-light);
    color: var(--ink);
  }
  .card--back {
    left: 627px;
    width: 370px;
    background: var(--card-dark);
  }
  .brand-square {
    position: absolute;
    left: 50%;
    transform: translateX(-50%);
  }
  .card--front .brand-square {
    top: 128px;
    width: 56px;
    height: 56px;
    background: var(--ink);
  }
  .card--back .brand-square {
    top: 196px;
    width: 72px;
    height: 72px;
    background: var(--paper);
  }
  .wordmark {
    position: absolute;
    left: 0;
    right: 0;
    text-align: center;
    font-weight: 400;
    letter-spacing: 0.3em;
    text-transform: uppercase;
    margin: 0;
    padding-left: 0.3em;
  }
  .card--front .wordmark {
    top: 226px;
    font-size: 31px;
    color: var(--ink);
  }
  .card--back .wordmark {
    top: 300px;
    font-size: 34px;
    color: var(--paper);
  }
  .holder {
    position: absolute;
    top: 382px;
    left: 0;
    right: 0;
    text-align: center;
  }
  .holder__name {
    margin: 0;
    font-size: 19px;
    font-weight: 600;
    line-height: 24px;
    color: var(--ink);
    text-transform: uppercase;
  }
  .holder__role {
    margin: 0;
    font-size: 16px;
    font-weight: 400;
    line-height: 18px;
    color: var(--ink-soft);
  }
  .contact-icons {
    position: absolute;
    top: 437px;
    left: 100px;
    width: 166px;
    height: 30px;
  }
  .contact-list {
    position: absolute;
    top: 472px;
    left: 0;
    right: 0;
    margin: 0;
    padding: 0;
    list-style: none;
    text-align: center;
    font-size: 17px;
    line-height: 22px;
    color: var(--ink-soft);
  }
</style>
</head>
<body>
<main class="canvas">
  <section class="card card--front" aria-label="Card front">
    <div class="brand-square" aria-hidden="true"></div>
    <h1 class="wordmark">Branvique</h1>
    <div class="holder">
      <p class="holder__name">Marcus Ellery</p>
      <p class="holder__role">Managing Director</p>
    </div>
    <svg class="contact-icons" viewBox="0 0 166 30" aria-hidden="true">
      <g fill="none" stroke="var(--ink)" stroke-width="1.3">
        <line x1="0" y1="15" x2="34" y2="15"/>
        <line x1="131" y1="15" x2="166" y2="15"/>
        <circle cx="48" cy="15" r="13"/>
        <circle cx="83" cy="15" r="13"/>
        <circle cx="118" cy="15" r="13"/>
      </g>
      <g fill="var(--ink)">
        <path d="M41 14 q7-6 14 0 v2 h-3 v-2 q-4-2-8 0 v2 h-3z"/>
        <rect x="42" y="16" width="12" height="6" rx="1"/>
      </g>
      <rect x="78.5" y="7.5" width="9" height="15" rx="1.5" fill="none" stroke="var(--ink)" stroke-width="1.5"/>
      <rect x="80.5" y="10" width="5" height="9" fill="var(--ink)"/>
      <rect x="111" y="10" width="14" height="10" fill="var(--ink)"/>
      <polyline points="111,10 118,16 125,10" fill="none" stroke="var(--card-light)" stroke-width="1.2"/>
    </svg>
    <ul class="contact-list">
      <li>555-382-6047</li>
      <li>555-731-5820</li>
      <li>name@branvique.com</li>
    </ul>
  </section>

  <section class="card card--back" aria-label="Card back">
    <div class="brand-square" aria-hidden="true"></div>
    <p class="wordmark">Branvique</p>
  </section>
</main>
</body>
</html>
```